Software company WebSite Design (enterprise level SW, Mobile apps, HW prototypes)

We need design for our new webpages. We got new logo and new business cards and we need webdesign which will be match with those two.
We are dealing with corporate level software development - enterprise level portals, development of optimalization SW, route planning optimalizations. For a few months we are developing mobile applications for companies.
IMPORTANT is to express the cutting edge technological company.

Target Market(s)

IT company customers

Industry/Entity Type

Business

Number of Pages Required

2 page

Requirements
Must have
• Project needs to have landing page and product detail page. Design needs to be created including full font and example images as there would be a real webpage. Design should be clean, modern and expressing hi-tech level of the company.
• Example of well designer web pages - www.quorvelt.com, www.brandissa.com - We like the font formatting and font designs (colors, placing, etc - its professional).
• Attached image contains screenshot from old web landing page. It contains basic sections of our business (Simulation Tools, Enterprise Intranet Systems, Hi-tech web presentations, Supporting Enterprise services - Optimalization and logistics monitoring)

```html
<!DOCTYPE html>
<html lang="en">
<head>
<meta charset="utf-8">
<title>Kestrova Solutions</title>
<link rel="stylesheet" href="https://fonts.googleapis.com/css2?family=Roboto:wght@300;400;500&family=Open+Sans:wght@400;600&display=swap">
<style>
:root{
  --blue:#1a8ad4;
  --orange:#f07b1d;
  --red:#e8442a;
  --dark:#333;
  --text:#555;
  --muted:#777;
  --band:#f4f4f4;
  --line:#dcdcdc;
  --green:#3aaa35;
  --purple:#7b3b8f;
  --star:#f5b800;
}
*{box-sizing:border-box;margin:0;padding:0}
html,body{width:1200px;height:2236px;overflow:hidden;background:#fff}
body{font-family:"Open Sans",Arial,sans-serif;color:var(--text);position:relative}
.heading{font-family:"Roboto",Arial,sans-serif;font-weight:300;color:var(--dark)}
section,header,footer{position:absolute;left:0;width:1200px}
.abs{position:absolute}

/* header */
.site-header{top:0;height:54px;background:#fff}
.brand{left:89px;top:12px;display:flex;align-items:center;gap:8px;font-family:"Roboto",sans-serif;font-weight:500;font-size:20px;color:#444;letter-spacing:1px}
.brand-square{width:26px;height:26px;background:var(--blue)}
.main-nav{left:0;top:0;width:1000px;height:54px;font-family:"Roboto",sans-serif;font-size:13px;color:#333}
.main-nav span{position:absolute;top:19px;white-space:nowrap}
.main-nav .drop::after{content:"";display:inline-block;margin-left:7px;border:4px solid transparent;border-top:5px solid #333;vertical-align:middle;transform:translateY(2px)}
.login{left:1011px;top:10px;width:100px;height:32px;background:var(--blue);color:#fff;font-family:"Roboto",sans-serif;font-size:13px;font-weight:500;display:flex;align-items:center;justify-content:center;border-radius:2px}

/* hero */
.hero{top:54px;height:553px;background:linear-gradient(135deg,#3a4250 0%,#2a313c 45%,#1f2530 100%);overflow:hidden}
.hero-frame{left:514px;top:176px}
.hero-title{top:222px;width:1200px;text-align:center;font-size:52px;color:#fff}
.hero-sub{top:291px;width:1200px;text-align:center;font-family:"Roboto",sans-serif;font-weight:300;font-size:19px;color:#eee}
.hero-wave{left:0;bottom:0}

/* services */
.services{top:607px;height:273px}
.service{width:240px;text-align:center}
.service svg{display:block;margin:0 auto}
.service h3{font-family:"Roboto",sans-serif;font-weight:400;font-size:16px;margin-top:14px}
.service p{font-size:12px;line-height:18px;color:var(--text);margin-top:6px}
.service .more{font-size:12px;margin-top:4px;display:block}

/* provide */
.provide{top:880px;height:357px;background:var(--band)}
.device-mock{left:89px;top:44px;width:496px;height:313px;background:linear-gradient(180deg,#ffffff 0%,#eef2e4 100%);border:1px solid #ddd}
.provide-text{left:644px;top:50px;width:450px}
.provide-text h2{font-size:25px}
.provide-text p{font-size:13px;line-height:20px;margin-top:8px}
.checks{list-style:none;margin-top:16px}
.checks li{display:flex;align-items:center;gap:12px;font-size:13px;height:25px;color:#444}
.provide-text .more{color:var(--blue);font-size:13px;display:block;margin:10px 0 0 33px}

/* testimonials */
.testimonials{top:1237px;height:265px}
.section-title{width:1200px;text-align:center;font-size:27px}
.photo-frame{left:182px;top:74px;width:138px;height:116px;border:2px solid var(--orange)}
.photo{left:191px;top:83px;width:138px;height:131px;background:linear-gradient(180deg,#8a8f96,#4d525b)}
.quote{left:362px;top:86px;width:652px;font-size:12.5px;line-height:22px;color:#444}
.stars{left:362px;top:176px;color:var(--star);font-size:13px;letter-spacing:1px}
.quote-name{left:365px;top:196px;font-size:15px;color:#555}

/* stats */
.stats{top:1502px;height:245px;background:var(--band)}
.stat{width:320px;text-align:center}
.stat-figure{height:70px;display:flex;align-items:center;justify-content:center}
.big-number{font-family:"Roboto",sans-serif;font-weight:300;font-size:62px;color:var(--orange);line-height:1}
.stat h3{font-family:"Roboto",sans-serif;font-weight:400;font-size:18px;color:var(--dark);margin-top:2px}
.stat h3 small{font-size:15px;color:#444}
.stat p{font-size:12px;line-height:18px;margin-top:10px}

/* customers */
.customers{top:1747px;height:188px}
.logo-row{left:89px;top:74px;display:flex;gap:8px}
.client{width:140px;height:61px;border:1px solid var(--line);display:flex;align-items:center;justify-content:center;font-family:"Roboto",sans-serif;font-weight:500;font-size:18px;color:#333}

/* footer */
.site-footer{top:1935px;height:255px;background:var(--band)}
.footer-brand{left:89px;top:30px;display:flex;align-items:center;gap:12px;font-family:"Roboto",sans-serif;font-weight:500;font-size:30px;color:#444;letter-spacing:1px}
.footer-brand .brand-square{width:44px;height:44px}
.footer-col h4{font-family:"Roboto",sans-serif;font-weight:400;font-size:16px;color:var(--dark);margin-bottom:6px}
.footer-col ul{list-style:none}
.footer-col li{font-size:12px;line-height:24px;color:#444}
.footer-col .dot li::before{content:"";display:inline-block;width:4px;height:4px;border-radius:50%;background:var(--orange);margin:0 9px 2px 0;vertical-align:middle}
.social{display:flex;gap:6px;margin-top:8px}
.social span{width:33px;height:33px;border-radius:50%}
.copyright{top:2190px;height:46px;background:#ececec;font-size:12px;color:#444;padding:17px 0 0 89px}
</style>
</head>
<body>

<header class="site-header">
  <div class="abs brand"><span class="brand-square"></span>Kestrova</div>
  <nav class="abs main-nav">
    <span class="drop" style="left:494px">Products</span>
    <span style="left:581px">Customers</span>
    <span style="left:672px">Pricing</span>
    <span style="left:741px">Developers</span>
    <span class="drop" style="left:836px">Support</span>
    <span class="drop" style="left:918px">Resources</span>
  </nav>
  <div class="abs login">Client Login</div>
</header>

<section class="hero" role="img" aria-label="Photo of two businessmen in suits working together at a desk">
  <svg class="abs hero-frame" width="174" height="194" viewBox="0 0 174 194" fill="none" stroke="var(--orange)" stroke-width="2">
    <path d="M1 52 V1 H173 V52"/>
    <path d="M1 146 V193 H173 V146"/>
  </svg>
  <h1 class="abs heading hero-title">Develop Experiences</h1>
  <p class="abs hero-sub">UI frameworks and app development tools that 1.9 million developers love</p>
  <svg class="abs hero-wave" width="1200" height="60" viewBox="0 0 1200 60">
    <path d="M0 60 L0 52 L520 52 C560 52 565 28 600 28 C635 28 640 52 680 52 L1200 52 L1200 60 Z" fill="#fff"/>
    <circle cx="600" cy="46" r="12" fill="none" stroke="#333" stroke-width="1.5"/>
    <path d="M594 44 L600 50 L606 44" fill="none" stroke="#333" stroke-width="1.5"/>
  </svg>
</section>

<section class="services">
  <div class="abs service" style="left:96px;top:36px">
    <svg width="84" height="84" viewBox="0 0 84 84"><rect x="14" y="14" width="56" height="56" transform="rotate(45 42 42)" fill="none" stroke="var(--blue)" stroke-width="1.5"/><rect x="33" y="31" width="18" height="22" fill="var(--blue)"/><g fill="#fff"><rect x="36" y="34" width="3" height="3"/><rect x="42" y="34" width="3" height="3"/><rect x="36" y="40" width="3" height="3"/><rect x="42" y="40" width="3" height="3"/><rect x="39" y="47" width="5" height="6"/></g></svg>
    <h3 style="color:var(--blue)">Enterprise portal</h3>
    <p>Lorem ipsum dolor sit amet, consectetuer adipiscing elit aenean commodo ligula eget dolor aenean .</p>
    <span class="more" style="color:var(--blue)">Read More</span>
  </div>
  <div class="abs service" style="left:352px;top:36px">
    <svg width="84" height="84" viewBox="0 0 84 84"><rect x="14" y="14" width="56" height="56" transform="rotate(45 42 42)" fill="none" stroke="var(--orange)" stroke-width="1.5"/><circle cx="43" cy="38" r="8" fill="none" stroke="var(--orange)" stroke-width="2.5"/><path d="M38 44 L32 52" stroke="var(--orange)" stroke-width="3"/></svg>
    <h3 style="color:var(--orange)">Optimalization SW</h3>
    <p>Lorem ipsum dolor sit amet, consectetuer adipiscing elit aenean commodo ligula eget dolor aenean .</p>
    <span class="more" style="color:var(--orange)">Read More</span>
  </div>
  <div class="abs service" style="left:607px;top:36px">
    <svg width="84" height="84" viewBox="0 0 84 84"><rect x="14" y="14" width="56" height="56" transform="rotate(45 42 42)" fill="none" stroke="var(--red)" stroke-width="1.5"/><rect x="33" y="32" width="18" height="20" fill="none" stroke="var(--red)" stroke-width="2"/><path d="M38 46 L48 35" stroke="var(--red)" stroke-width="2"/></svg>
    <h3 style="color:var(--red)">Route planing optimalization</h3>
    <p>Lorem ipsum dolor sit amet, consectetuer adipiscing elit aenean commodo ligula eget dolor aenean .</p>
    <span class="more" style="color:var(--red)">Read More</span>
  </div>
  <div class="abs service" style="left:863px;top:36px">
    <svg width="84" height="84" viewBox="0 0 84 84"><rect x="14" y="14" width="56" height="56" transform="rotate(45 42 42)" fill="none" stroke="#333" stroke-width="1.5"/><rect x="36" y="29" width="12" height="24" rx="2" fill="#333"/><rect x="38" y="32" width="8" height="16" fill="#fff"/></svg>
    <h3 style="color:#333">Mobile applications</h3>
    <p>Lorem ipsum dolor sit amet, consectetuer adipiscing elit aenean commodo ligula eget dolor aenean .</p>
    <span class="more" style="color:#333">Read More</span>
  </div>
</section>

<section class="provide">
  <div class="abs device-mock" role="img" aria-label="Analytics dashboard shown on a laptop screen and a smartphone"></div>
  <div class="abs provide-text">
    <h2 class="heading">What we provide</h2>
    <p>Lorem ipsum dolor sit amet, consectetuer adipiscing elit. Aenean commodo ligula eget dolor aenean massa.</p>
    <ul class="checks">
      <li><svg width="19" height="19" viewBox="0 0 19 19"><circle cx="9.5" cy="9.5" r="9.5" fill="var(--blue)"/><path d="M5 10 L8.3 13 L14 6.5" fill="none" stroke="#fff" stroke-width="2"/></svg>Simulation Tools</li>
      <li><svg width="19" height="19" viewBox="0 0 19 19"><circle cx="9.5" cy="9.5" r="9.5" fill="var(--blue)"/><path d="M5 10 L8.3 13 L14 6.5" fill="none" stroke="#fff" stroke-width="2"/></svg>Enterprise Intranet Systems</li>
      <li><svg width="19" height="19" viewBox="0 0 19 19"><circle cx="9.5" cy="9.5" r="9.5" fill="var(--blue)"/><path d="M5 10 L8.3 13 L14 6.5" fill="none" stroke="#fff" stroke-width="2"/></svg>Hi-tech web presentations</li>
      <li><svg width="19" height="19" viewBox="0 0 19 19"><circle cx="9.5" cy="9.5" r="9.5" fill="var(--blue)"/><path d="M5 10 L8.3 13 L14 6.5" fill="none" stroke="#fff" stroke-width="2"/></svg>Supporting Enterprise services</li>
      <li><svg width="19" height="19" viewBox="0 0 19 19"><circle cx="9.5" cy="9.5" r="9.5" fill="var(--blue)"/><path d="M5 10 L8.3 13 L14 6.5" fill="none" stroke="#fff" stroke-width="2"/></svg>Optimalization</li>
      <li><svg width="19" height="19" viewBox="0 0 19 19"><circle cx="9.5" cy="9.5" r="9.5" fill="var(--blue)"/><path d="M5 10 L8.3 13 L14 6.5" fill="none" stroke="#fff" stroke-width="2"/></svg>logistics monitoring</li>
    </ul>
    <span class="more">Read More</span>
  </div>
</section>

<section class="testimonials">
  <h2 class="abs heading section-title" style="top:36px">Testimonials</h2>
  <div class="abs photo-frame"></div>
  <div class="abs photo" role="img" aria-label="Photo of a young man sitting on a sofa with a laptop"></div>
  <p class="abs quote">Lorem ipsum dolor sit amet, consectetuer adipiscing elit. Aenean commodo ligula eget dolor. Aenean massa. Cum sociis natoque penatibus et magnis dis parturient montes, nascetur ridiculus mus. Donec quam felis, ultricies nec, pellentesque eu, pretium quis, sem. Nulla consequat massa quis enim. Lorem ipsum dolor sit amet, consectetuer adipiscing elit. Aenean commodo ligula eget dolor.</p>
  <div class="abs stars">★★★★★</div>
  <div class="abs quote-name">John Doe</div>
</section>

<section class="stats">
  <div class="abs stat" style="left:101px;top:36px">
    <div class="stat-figure"><span class="big-number">27 +</span></div>
    <h3>27+ <small>years in technological Company</small></h3>
    <p>Lorem ipsum dolor sit amet, consectetuer adipiscing elit.<br>Aenean commodo ligula eget dolor aenean massa.<br>Cum sociis natoque penatibus .</p>
  </div>
  <div class="abs stat" style="left:442px;top:36px">
    <div class="stat-figure"><svg width="56" height="52" viewBox="0 0 56 52" fill="none" stroke="var(--green)" stroke-width="2"><circle cx="28" cy="17" r="11"/><path d="M10 50 C10 36 18 31 28 31 C38 31 46 36 46 50 Z"/><circle cx="11" cy="22" r="6"/><circle cx="45" cy="22" r="6"/><path d="M2 44 C2 36 6 32 12 32"/><path d="M54 44 C54 36 50 32 44 32"/></svg></div>
    <h3>450+ <small>employees</small></h3>
    <p>Lorem ipsum dolor sit amet, consectetuer adipiscing elit.<br>Aenean commodo ligula eget dolor aenean massa.<br>Cum sociis natoque penatibus .</p>
  </div>
  <div class="abs stat" style="left:782px;top:36px">
    <div class="stat-figure"><svg width="60" height="52" viewBox="0 0 60 52" fill="none" stroke="var(--purple)" stroke-width="2"><rect x="2" y="12" width="56" height="38"/><path d="M21 12 V4 H39 V12"/><path d="M2 26 H58"/><rect x="26" y="22" width="8" height="8"/></svg></div>
    <h3>1200+ <small>completed projects</small></h3>
    <p>Lorem ipsum dolor sit amet, consectetuer adipiscing elit.<br>Aenean commodo ligula eget dolor aenean massa.<br>Cum sociis natoque penatibus .</p>
  </div>
</section>

<section class="customers">
  <h2 class="abs heading section-title" style="top:24px">Our Customers</h2>
  <div class="abs logo-row">
    <div class="client">Orbiqa</div>
    <div class="client">Lumenhart</div>
    <div class="client">Vantello</div>
    <div class="client">Sorivo</div>
    <div class="client">Brixel</div>
    <div class="client">Tamarind</div>
    <div class="client">Velmora</div>
  </div>
</section>

<footer class="site-footer">
  <div class="abs footer-brand"><span class="brand-square"></span>Kestrova</div>
  <div class="abs footer-col" style="left:358px;top:38px">
    <h4>Services</h4>
    <ul class="dot"><li>Enterprise portal</li><li>Optimalization SW</li><li>Route planing optimalization</li><li>Mobile applications</li></ul>
  </div>
  <div class="abs footer-col" style="left:626px;top:38px">
    <h4>About</h4>
    <ul class="dot"><li>Company</li><li>Team</li><li>Delivery Models</li><li>IP Protection</li><li>Development Process</li><li>Quality Management System</li></ul>
  </div>
  <div class="abs footer-col" style="left:872px;top:38px">
    <h4>Contact Us</h4>
    <ul><li>Contact Information</li><li>Become Kestrova Solutions Partner</li><li>Request for Quote</li></ul>
    <div class="social"><span style="background:#2d5a9e"></span><span style="background:#2aa9e0"></span><span style="background:#d23c2c"></span></div>
  </div>
</footer>

<div class="abs copyright" style="left:0;width:1200px">Copyright 2016 | All Right Reserved</div>

</body>
</html>
```